Company Banner

I would like our 5 corporate Core Values placed on a single banner that has a theme related to our engineering industry.

Core Values: Productive & Hard Working, Professional, Humble, Personable, Adaptable

Target Market(s)

Construction, Engineering

Requirements
Must have
• All words randomly positioned on the banner with color and industry background images.

Please add company logo to upper left corner as well (attached logo design file)

```html
<!DOCTYPE html>
<html lang="en">
<head>
<meta charset="utf-8">
<title>Core Values Banner</title>
<link href="https://fonts.googleapis.com/css2?family=Bebas+Neue&family=Roboto:wght@300;500&display=swap" rel="stylesheet">
<style>
  :root {
    --navy: #0d1226;
    --white: #ffffff;
    --black: #000000;
    --orange: #ffa300;
    --orange-soft: #d9790f;
    --mustard: #dccd07;
    --mustard-soft: #fbe94a;
    --blue: #0392ea;
    --blue-soft: #3bd3ff;
    --green: #69c404;
    --green-soft: #a9f52a;
    --olive: #7f7f00;
    --olive-soft: #c8c114;
    --brand: #3a3f48;
    --photo-light: #eeeeee;
    --photo-mid: #d6d6d6;
  }
  html, body {
    margin: 0;
    padding: 0;
    width: 1200px;
    height: 2218px;
    overflow: hidden;
    background: var(--navy);
  }
  .canvas {
    position: relative;
    width: 1200px;
    height: 2218px;
  }
  .banner {
    position: absolute;
    left: 113px;
    width: 975px;
    height: 949px;
    display: block;
  }
  .banner--plain { top: 111px; }
  .banner--photo { top: 1158px; }
  .value-label {
    font-family: 'Bebas Neue', sans-serif;
    font-size: 38px;
    fill: var(--white);
    text-anchor: middle;
  }
  .core-title {
    font-family: 'Bebas Neue', sans-serif;
    font-size: 112px;
    fill: var(--white);
    text-anchor: middle;
  }
  .core-subtitle {
    font-family: 'Roboto', sans-serif;
    font-weight: 300;
    font-size: 40px;
    letter-spacing: 8px;
    fill: var(--white);
    text-anchor: middle;
  }
  .brand-name {
    font-family: 'Roboto', sans-serif;
    font-weight: 500;
    fill: var(--brand);
    text-anchor: end;
  }
</style>
</head>
<body>
<div class="canvas">

  <svg class="banner banner--plain" viewBox="0 0 975 949" xmlns="http://www.w3.org/2000/svg">
    <rect class="banner-bg" width="975" height="949" fill="var(--white)"/>

    <g class="brand">
      <text class="brand-name" x="889" y="132" font-size="36">KESTREL</text>
      <text class="brand-name" x="889" y="166" font-size="28" letter-spacing="2">GROUP</text>
      <text class="brand-name" x="889" y="198" font-size="28" letter-spacing="2">INC.</text>
    </g>

    <g class="value value--productive">
      <circle cx="483" cy="204" r="108.5" fill="var(--orange)"/>
      <ellipse role="img" aria-label="Drilling rig icon" cx="513" cy="260" rx="34" ry="48" fill="var(--orange-soft)" opacity="0.35"/>
      <text class="value-label" x="483" y="199">PRODUCTIVE &amp;</text>
      <text class="value-label" x="487" y="235">HARD WORKING</text>
    </g>

    <g class="value value--humble">
      <circle cx="186" cy="429" r="108.5" fill="var(--mustard)"/>
      <ellipse role="img" aria-label="Hand holding a gear icon" cx="190" cy="490" rx="52" ry="36" fill="var(--mustard-soft)" opacity="0.5"/>
      <text class="value-label" x="184" y="443">HUMBLE</text>
    </g>

    <g class="value value--professional">
      <circle cx="788" cy="429" r="108.5" fill="var(--blue)"/>
      <ellipse role="img" aria-label="Engineer in hard hat icon" cx="788" cy="490" rx="58" ry="44" fill="var(--blue-soft)" opacity="0.45"/>
      <text class="value-label" x="790" y="443">PROFESSIONAL</text>
    </g>

    <g class="value value--core">
      <circle cx="483" cy="494" r="152.5" fill="var(--black)"/>
      <text class="core-title" x="480" y="513">CORE</text>
      <text class="core-subtitle" x="487" y="564">VALUES</text>
    </g>

    <g class="value value--personable">
      <circle cx="319" cy="745" r="108.5" fill="var(--green)"/>
      <ellipse role="img" aria-label="Worker with wrench icon" cx="319" cy="805" rx="50" ry="42" fill="var(--green-soft)" opacity="0.5"/>
      <text class="value-label" x="319" y="759">PERSONABLE</text>
    </g>

    <g class="value value--adaptable">
      <circle cx="647" cy="745" r="108.5" fill="var(--olive)"/>
      <ellipse role="img" aria-label="Two gears icon" cx="672" cy="797" rx="64" ry="38" fill="var(--olive-soft)" opacity="0.45"/>
      <text class="value-label" x="647" y="759">ADAPTABLE</text>
    </g>
  </svg>

  <svg class="banner banner--photo" viewBox="0 0 975 949" xmlns="http://www.w3.org/2000/svg">
    <defs>
      <linearGradient id="workshop-tone" x1="0" y1="0" x2="0" y2="1">
        <stop offset="0" stop-color="var(--photo-mid)"/>
        <stop offset="0.55" stop-color="#e2e1de"/>
        <stop offset="0.72" stop-color="#ece6da"/>
        <stop offset="1" stop-color="var(--photo-light)"/>
      </linearGradient>
    </defs>
    <rect role="img" aria-label="Faded photo of a worker grinding metal with sparks" width="975" height="949" fill="url(#workshop-tone)"/>

    <g class="brand">
      <text class="brand-name" x="889" y="132" font-size="36">KESTREL</text>
      <text class="brand-name" x="889" y="166" font-size="28" letter-spacing="2">GROUP</text>
      <text class="brand-name" x="889" y="198" font-size="28" letter-spacing="2">INC.</text>
    </g>

    <g class="value value--productive">
      <circle cx="483" cy="204" r="108.5" fill="var(--orange)"/>
      <ellipse role="img" aria-label="Drilling rig icon" cx="513" cy="260" rx="34" ry="48" fill="var(--orange-soft)" opacity="0.35"/>
      <text class="value-label" x="483" y="199">PRODUCTIVE &amp;</text>
      <text class="value-label" x="487" y="235">HARD WORKING</text>
    </g>

    <g class="value value--humble">
      <circle cx="186" cy="429" r="108.5" fill="var(--mustard)"/>
      <ellipse role="img" aria-label="Hand holding a gear icon" cx="190" cy="490" rx="52" ry="36" fill="var(--mustard-soft)" opacity="0.5"/>
      <text class="value-label" x="184" y="443">HUMBLE</text>
    </g>

    <g class="value value--professional">
      <circle cx="788" cy="429" r="108.5" fill="var(--blue)"/>
      <ellipse role="img" aria-label="Engineer in hard hat icon" cx="788" cy="490" rx="58" ry="44" fill="var(--blue-soft)" opacity="0.45"/>
      <text class="value-label" x="790" y="443">PROFESSIONAL</text>
    </g>

    <g class="value value--core">
      <circle cx="483" cy="494" r="152.5" fill="var(--black)"/>
      <text class="core-title" x="480" y="513">CORE</text>
      <text class="core-subtitle" x="487" y="564">VALUES</text>
    </g>

    <g class="value value--personable">
      <circle cx="319" cy="745" r="108.5" fill="var(--green)"/>
      <ellipse role="img" aria-label="Worker with wrench icon" cx="319" cy="805" rx="50" ry="42" fill="var(--green-soft)" opacity="0.5"/>
      <text class="value-label" x="319" y="759">PERSONABLE</text>
    </g>

    <g class="value value--adaptable">
      <circle cx="647" cy="745" r="108.5" fill="var(--olive)"/>
      <ellipse role="img" aria-label="Two gears icon" cx="672" cy="797" rx="64" ry="38" fill="var(--olive-soft)" opacity="0.45"/>
      <text class="value-label" x="647" y="759">ADAPTABLE</text>
    </g>
  </svg>

</div>
</body>
</html>
```